Updating our Raw Materials Brochure

Please update and modify (to add more space for the additional text) the brochure designed for us in January (see attached file) so we can circulate a May 2021 version. Thanks and hope your family is OK despite the terrible tragedy going on with Covid-19 in India. Best wishes!

```html
<!DOCTYPE html>
<html lang="en">
<head>
<meta charset="utf-8">
<title>Raw Materials – May 2021 Market Update</title>
<link href="https://fonts.googleapis.com/css2?family=Open+Sans:wght@400;600;700;800&family=Roboto+Condensed:wght@400;700&display=swap" rel="stylesheet">
<style>
:root{
  --backdrop:#d8d9da;
  --paper:#ffffff;
  --panel:#efefef;
  --ink:#3a3a3a;
  --muted:#666;
  --red:#e8202a;
  --blue:#5aa9e6;
  --navy:#2b4fa0;
  --chart-orange:#ee7d22;
  --chart-blue:#4472c4;
  --band-blue:#8fb0de;
  --space-dark:#0d1320;
  --space-mid:#2a3345;
}
*{box-sizing:border-box;margin:0;padding:0}
html,body{width:1200px;height:788px;overflow:hidden}
body{background:var(--backdrop);font-family:"Open Sans",sans-serif;color:var(--ink);position:relative}
.page{position:absolute;background:var(--paper);overflow:hidden;box-shadow:0 2px 6px rgba(0,0,0,.25)}
.page--front{left:77px;top:54px;width:504px;height:652px}
.page--back{left:619px;top:52px;width:506px;height:654px}

.masthead{position:absolute;left:0;top:0;width:100%;height:83px;background:var(--paper)}
.brand{position:absolute;display:flex;align-items:center;gap:6px;font-family:"Open Sans",sans-serif;font-weight:800;color:#2d2d2d;letter-spacing:.3px;white-space:nowrap}
.brand__dot{width:11px;height:11px;border-radius:50%;background:#8a8a8a;flex:none}
.masthead .brand{left:34px;top:33px;font-size:13.5px}
.call-box{position:absolute;left:240px;top:18px;width:264px;height:54px;background:var(--red);clip-path:polygon(10% 0,100% 0,100% 100%,0 100%);color:#fff;display:flex;align-items:center;padding-left:40px;gap:8px}
.call-box svg{width:14px;height:22px;flex:none}
.call-box__text{font-size:15px;line-height:16px}
.call-box__text b{font-weight:800;display:block;font-size:16px}

.hero{position:absolute;left:0;width:100%;background:radial-gradient(ellipse at 50% 120%,#3d5b86 0%,var(--space-mid) 30%,var(--space-dark) 70%);color:#fff;text-align:center}
.page--front .hero{top:83px;height:147px}
.page--back .hero{top:0;height:192px}
.hero__title{font-weight:700;font-size:40px;line-height:43px;letter-spacing:1px}
.hero__sub{font-family:"Roboto Condensed",sans-serif;font-weight:700;color:var(--red);font-size:30px;letter-spacing:12px;line-height:32px}
.page--front .hero__title:first-child{padding-top:20px}
.page--back .brand{position:relative;justify-content:center;padding-top:26px;font-size:15px;color:#fff}
.page--back .brand__dot{background:#fff}
.page--back .hero__title:nth-child(2){margin-top:4px}

.col{position:absolute}
.col--panel{background:var(--panel)}
.tag-blue{display:inline-block;background:var(--blue);color:#fff;font-family:"Roboto Condensed",sans-serif;font-weight:700;padding:2px 22px 2px 8px;clip-path:polygon(0 0,94% 0,100% 100%,0 100%);border-left:5px solid #333;white-space:nowrap}
.tag-red{background:var(--red);color:#fff;font-family:"Roboto Condensed",sans-serif;font-weight:700;text-align:center}
.subhead{color:var(--red);font-family:"Roboto Condensed",sans-serif;font-weight:700;font-size:8.5px;text-align:center;line-height:9.5px}
.body-copy p{font-size:7px;line-height:8.7px;text-align:justify;margin-bottom:8px}
.chart-title{font-size:8px;color:#555;text-align:center}
svg text{font-family:"Open Sans",sans-serif}
.footer-strip{position:absolute;left:0;bottom:0;width:100%;height:9px;background:var(--band-blue)}
.footer-call{position:absolute;left:0;bottom:0;width:100%;height:56px;background:var(--red);color:#fff;display:flex;align-items:center;justify-content:center;gap:10px;font-size:23px}
.footer-call b{font-weight:800}
.footer-call svg{width:16px;height:26px}
</style>
</head>
<body>

<!-- Front page -->
<section class="page page--front">
  <header class="masthead">
    <div class="brand"><span class="brand__dot"></span>NORTHBOND INDUSTRIES</div>
    <div class="call-box">
      <svg viewBox="0 0 14 22"><path d="M11 1 C3 3 2 19 11 21" fill="none" stroke="#fff" stroke-width="2.4" stroke-linecap="round"/></svg>
      <div class="call-box__text">Call us at<b>800-555-BOND (2663)</b></div>
    </div>
  </header>
  <div class="hero" role="img" aria-label="Photo of Earth seen from space at sunrise">
    <div class="hero__title">RAW MATERIALS</div>
    <div class="hero__title">MAY 2021</div>
    <div class="hero__sub">MARKET UPDATE</div>
  </div>

  <div class="col" style="left:0;top:230px;width:258px;height:413px">
    <div class="tag-blue" style="margin-top:17px;font-size:16px;width:235px">GLOBAL SHORTAGES</div>
    <div class="body-copy" style="padding:8px 10px 0 11px">
      <p>As the recovery builds momentum more manufacturers are trying to buy extra material to prevent running out. Nearly all inputs are affected and there seems to be no end in sight as supply is unable to keep up with demand.</p>
      <p>The situation has been complicated by a growing list of disasters. Starting with the deep freeze and blackouts wiping out energy and petrochemicals operations in February, the Suez canal back up in March then hackers bringing down the largest US pipeline this month.</p>
      <p>US GDP increased at a 10.7% annual rate or $554.2 billion in current dollars (adjusted to 6.4% for inflation) in the first quarter. Demand seems to be driven by personal income growing $2.4 trillion (up 59%) from increased government social benefits and pandemic relief programs. Expectations are it will continue as personal savings were $4.12 trillion (up 83% the fourth quarter) driving personal savings to 21%.</p>
      <p>The trailing 12-month Producer Price Index and Consumer Price Index were up 6.2% and 4.2% respectively. These should go higher as the trailing 4-months averages are 10.2% and 6.3% respectively. Our procurement team is focused on leveraging our global supply position and growing demand so we will continue to deliver you the most competitive costs available despite these conditions.</p>
    </div>
    <svg style="position:absolute;left:12px;top:297px" width="240" height="112" viewBox="0 0 240 112">
      <text x="0" y="5" font-size="3.6" font-weight="700" fill="#333">Chart 2. 12-month percent change in CPI, all urban consumers, Apr 2020 – Apr 2021</text>
      <text x="0" y="10" font-size="3.2" fill="#555">Percent change</text>
      <g stroke="#ddd" stroke-width=".4">
        <line x1="14" y1="18" x2="236" y2="18"/><line x1="14" y1="33" x2="236" y2="33"/><line x1="14" y1="48" x2="236" y2="48"/><line x1="14" y1="63" x2="236" y2="63"/><line x1="14" y1="78" x2="236" y2="78"/><line x1="14" y1="93" x2="236" y2="93"/>
      </g>
      <g font-size="3.5" fill="#555"><text x="8" y="19">5</text><text x="8" y="34">4</text><text x="8" y="49">3</text><text x="8" y="64">2</text><text x="8" y="79">1</text><text x="8" y="94">0</text></g>
      <polyline fill="none" stroke="#7b6fd1" stroke-width=".9" points="18,88 35,92 52,85 69,78 86,74 103,74 120,76 137,76 154,73 171,74 188,69 205,60 222,41"/>
      <polyline fill="none" stroke="#c0394b" stroke-width=".9" points="18,75 35,78 52,78 69,72 86,71 103,71 120,72 137,72 154,72 171,72 188,75 205,70 222,54"/>
      <g font-size="3.2" fill="#555"><text x="12" y="100">Apr20</text><text x="32" y="100">May</text><text x="50" y="100">Jun</text><text x="67" y="100">Jul</text><text x="84" y="100">Aug</text><text x="101" y="100">Sep</text><text x="118" y="100">Oct</text><text x="135" y="100">Nov</text><text x="152" y="100">Dec</text><text x="169" y="100">Jan</text><text x="186" y="100">Feb</text><text x="203" y="100">Mar</text><text x="218" y="100">Apr21</text></g>
      <g font-size="3.2" fill="#555"><line x1="56" y1="107" x2="66" y2="107" stroke="#7b6fd1"/><text x="70" y="108">All items</text><line x1="130" y1="107" x2="140" y2="107" stroke="#c0394b"/><text x="144" y="108">All items less food and energy</text></g>
    </svg>
  </div>

  <div class="col col--panel" style="left:257px;top:230px;width:247px;height:413px">
    <div class="tag-red" style="margin:17px 0 0 0;height:22px;font-size:16px;line-height:22px">KEY CONSTRAINTS</div>
    <div class="subhead" style="margin-top:9px">ETHYLENE SHORTAGE DRIVES PRICES HIGHER</div>
    <div class="body-copy" style="padding:7px 8px 0 8px">
      <p>Contractual prices for Ethylene (key feedstock for water based and hot melt adhesives) increased 56% from 2020 to a 7-year high of $0.47/lb in March as multiple severe weather cracker outages driven by the deep freeze in February forced 70% capacity offline. Restarting production has been difficult as so many sites were damaged simultaneously.</p>
    </div>
    <div class="chart-title" style="margin-top:2px">Ethylene, Contract and Spot Pricing</div>
    <svg style="display:block;margin:2px 0 0 4px" width="240" height="118" viewBox="0 0 240 118">
      <g font-size="4.5" fill="#666">
        <text x="2" y="6">$0.650</text><text x="2" y="13">$0.600</text><text x="2" y="20">$0.550</text><text x="2" y="27">$0.500</text><text x="2" y="34">$0.450</text><text x="2" y="41">$0.400</text><text x="2" y="48">$0.350</text><text x="2" y="55">$0.300</text><text x="2" y="62">$0.250</text><text x="2" y="69">$0.200</text><text x="2" y="76">$0.150</text><text x="2" y="83">$0.100</text><text x="2" y="90">$0.050</text><text x="2" y="97">$0.000</text>
      </g>
      <polyline fill="none" stroke="var(--chart-blue)" stroke-width="1.1" points="44,52 82,53 118,51 154,41 192,41 228,26"/>
      <polyline fill="none" stroke="var(--chart-orange)" stroke-width="1.1" points="44,60 82,63 118,56 154,39 192,40 228,8"/>
      <g font-size="4.5" fill="#666"><text x="38" y="106">Oct-20</text><text x="76" y="106">Nov-20</text><text x="112" y="106">Dec-20</text><text x="148" y="106">Jan-21</text><text x="186" y="106">Feb-21</text><text x="222" y="106">Mar-21</text></g>
      <g font-size="3.8" fill="#666"><line x1="14" y1="114" x2="30" y2="114" stroke="var(--chart-blue)"/><text x="32" y="115.5">Meridian Index Contract NA Ethylene</text><line x1="145" y1="114" x2="161" y2="114" stroke="var(--chart-orange)"/><text x="163" y="115.5">Meridian Index Spot C2</text></g>
    </svg>
    <div class="subhead" style="margin-top:10px">VINYL ACETATE MONOMER (VAM) – KEY INGREDIENT<br>FOR WATER BASED ADHESIVES</div>
    <div class="body-copy" style="padding:6px 8px 0 8px">
      <p>VAM shortages became severe following the February winter storm driving prices up 128% since Jan-2021. All three US suppliers (Calvera, Dornway and Lindqvist Chem) declared force majeure and all four production sites were shut down. They were stuck in varying stages of restarting and ramping up to full rates for nearly 3 months so supplies remain limited and that is expected to continue through Q2 with demand currently outstripping supply.</p>
    </div>
  </div>
  <div class="footer-strip"></div>
</section>

<!-- Back page -->
<section class="page page--back">
  <div class="hero" role="img" aria-label="Photo of Earth seen from space at sunrise">
    <div class="brand"><span class="brand__dot"></span>NORTHBOND INDUSTRIES</div>
    <div class="hero__title">RAW MATERIALS</div>
    <div class="hero__title">MAY 2021</div>
    <div class="hero__sub">MARKET UPDATE</div>
  </div>

  <div class="col" style="left:0;top:192px;width:266px;height:406px">
    <div class="tag-blue" style="margin:11px 0 0 3px;font-size:10.5px;width:250px">LOGISTICS LIMITATIONS VS. DEMAND GROWTH</div>
    <div class="body-copy" style="padding:9px 10px 0 10px">
      <p>The ramp up in production of consumer and industrial goods while consumers still rely more on at home delivery or pick up from stores (which require more trucks and warehousing) has driven unprecedented logistics tightness.</p>
    </div>
    <svg style="position:absolute;left:10px;top:90px" width="252" height="128" viewBox="0 0 252 128">
      <text x="2" y="5" font-size="5.5" font-weight="700" fill="#222">A Logistical Nightmare</text>
      <text x="2" y="11" font-size="4.8" fill="#333">Transport, storage and inventory costs are near record highs in the U.S.</text>
      <g font-size="3.8" fill="#444"><line x1="2" y1="17" x2="6" y2="14" stroke="#222"/><text x="8" y="17">Transportation</text><line x1="46" y1="17" x2="50" y2="14" stroke="#e0457b"/><text x="52" y="17">Warehousing</text><line x1="88" y1="17" x2="92" y2="14" stroke="#3fa9e0"/><text x="94" y="17">Inventories</text></g>
      <text x="214" y="24" font-size="3.8" fill="#333">100 index level*</text>
      <g font-size="4.5" fill="#444"><text x="238" y="52">75</text><text x="238" y="80">50</text><text x="238" y="107">25</text></g>
      <line x1="2" y1="78" x2="234" y2="78" stroke="#b9b37a" stroke-width=".6" stroke-dasharray="2 1.5"/>
      <text x="60" y="44" font-size="4.2" fill="#333">Expansion</text>
      <text x="98" y="95" font-size="4.2" fill="#333">Contraction</text>
      <polyline fill="none" stroke="#222" stroke-width=".8" points="4,46 20,44 36,47 52,45 68,48 84,46 100,49 116,47 132,50 148,52 156,60 164,66 170,55 178,46 190,40 206,35 222,32 234,30"/>
      <polyline fill="none" stroke="#e0457b" stroke-width=".8" points="4,52 20,50 36,54 52,51 68,55 84,52 100,56 116,54 132,58 148,58 156,56 164,52 172,49 186,50 200,46 216,44 232,41"/>
      <polyline fill="none" stroke="#3fa9e0" stroke-width=".8" points="4,58 20,60 36,62 52,59 68,63 84,61 100,65 116,68 132,70 148,72 156,80 162,92 168,84 176,70 190,60 206,55 220,50 232,46"/>
      <g font-size="4.5" fill="#444"><text x="34" y="115">2019</text><text x="130" y="115">2020</text><text x="224" y="115">2021</text></g>
      <text x="2" y="121" font-size="3.3" fill="#444">Source: Freight Conditions Index</text>
      <text x="2" y="126" font-size="3.3" fill="#444">*The index is a diffusion index where 50 is the dividing line between expansion and contraction.</text>
    </svg>
    <div class="body-copy" style="position:absolute;left:10px;top:228px;width:246px">
      <p>Capacity is constrained by slowed construction in vehicles (chips and other materials shortages) as traditional channels are idled (shopping malls, etc.). Spot Van rates were up 58.1% versus April 2020 as outages cause chain reactions. Currently there is a traffic jam of 771 barges accumulated on the lower Mississippi due to a fractured bridge, so expectations are this will continue until year end</p>
    </div>
    <svg style="position:absolute;left:10px;top:292px" width="250" height="112" viewBox="0 0 250 112">
      <text x="96" y="4" font-size="4.2" font-weight="700" fill="#333">Transportation Prices</text>
      <g fill="#2e75c6">
        <rect x="8" y="58" width="5" height="40"/><rect x="17" y="60" width="5" height="38"/><rect x="26" y="64" width="5" height="34"/><rect x="35" y="62" width="5" height="36"/><rect x="44" y="61" width="5" height="37"/><rect x="53" y="64" width="5" height="34"/><rect x="62" y="68" width="5" height="30"/><rect x="71" y="57" width="5" height="41"/><rect x="80" y="57" width="5" height="41"/><rect x="89" y="60" width="5" height="38"/><rect x="98" y="63" width="5" height="35"/><rect x="107" y="50" width="5" height="48"/><rect x="116" y="70" width="5" height="28"/><rect x="125" y="62" width="5" height="36"/><rect x="134" y="46" width="5" height="52"/><rect x="143" y="38" width="5" height="60"/><rect x="152" y="32" width="5" height="66"/><rect x="161" y="27" width="5" height="71"/><rect x="170" y="28" width="5" height="70"/><rect x="179" y="26" width="5" height="72"/><rect x="188" y="30" width="5" height="68"/><rect x="197" y="27" width="5" height="71"/><rect x="206" y="25" width="5" height="73"/><rect x="215" y="26" width="5" height="72"/><rect x="224" y="23" width="5" height="75"/><rect x="233" y="22" width="5" height="76"/><rect x="242" y="21" width="5" height="77"/>
      </g>
      <polyline fill="none" stroke="#e8202a" stroke-width=".7" stroke-dasharray="1.5 1" points="10,55 19,57 28,61 37,59 46,58 55,61 64,65 73,54 82,54 91,57 100,60 109,47 118,67 127,59 136,43 145,35 154,29 163,24 172,25 181,23 190,27 199,24 208,22 217,23 226,20 235,19 244,18"/>
      <g font-size="3" fill="#444"><text x="4" y="106">Apr19</text><text x="58" y="106">Oct19</text><text x="112" y="106">Apr20</text><text x="166" y="106">Oct20</text><text x="226" y="106">Apr21</text></g>
    </svg>
  </div>

  <div class="col col--panel" style="left:266px;top:192px;width:240px;height:406px">
    <svg style="display:block;margin:4px 0 0 4px" width="232" height="134" viewBox="0 0 232 134">
      <text x="100" y="10" font-size="7.5" fill="#555">VAM Index</text>
      <g font-size="4.5" fill="#777"><text x="2" y="24">$2,300.0</text><text x="2" y="34.5">$2,100.0</text><text x="2" y="45">$1,900.0</text><text x="2" y="55.5">$1,700.0</text><text x="2" y="66">$1,500.0</text><text x="2" y="76.5">$1,300.0</text><text x="2" y="87">$1,100.0</text><text x="2" y="97.5">$900.0</text><text x="2" y="108">$700.0</text><text x="2" y="118.5">$500.0</text></g>
      <polyline fill="none" stroke="var(--chart-orange)" stroke-width="1.1" points="46,96 80,95.5 112,95.5 144,95 160,92 180,70 200,58 222,43"/>
      <g font-size="4.5" fill="#777"><text x="40" y="127">Oct-20</text><text x="70" y="127">Nov-20</text><text x="100" y="127">Dec-20</text><text x="130" y="127">Jan-21</text><text x="160" y="127">Feb-21</text><text x="190" y="127">Mar-21</text><text x="216" y="127">Apr-21</text></g>
      <line x1="70" y1="132" x2="82" y2="132" stroke="var(--chart-orange)"/><text x="84" y="133.5" font-size="3.8" fill="#777">Meridian VAM FOB Spot Low ($/mt)</text>
    </svg>
    <div class="tag-red" style="margin-top:8px;height:30px;font-size:11px;line-height:13px;padding-top:3px">POLYETHYLENE AND POLYURETHANE<br>PRICES NEAR RECORD HIGHS</div>
    <div class="body-copy" style="padding:6px 8px 0 8px">
      <p>About 42% of US oil refining capacity went offline in February (~5.5m barrels/day) but it has recovered to over 86% by last week. The shortages this created downstream continue to create spot outages of critical inputs resulting in reduced operating rates at our suppliers.</p>
      <p>For example, Polyethylene polymers (critical in hot melt adhesives) increased 39% this year plus Benzene increased 10% in April and Polyether Polyols (key feedstock for polyurethanes) are on 75% sales allocation because of limited domestic materials and difficulty bringing in imports from marine transport shortages. As a result, the price index for rubbers and plastics is up 9% since January and is still rising.</p>
    </div>
    <svg style="position:absolute;left:4px;top:306px" width="232" height="98" viewBox="0 0 232 98">
      <rect x="0" y="0" width="232" height="98" fill="#fff"/>
      <text x="3" y="7" font-size="5.5" font-weight="700" fill="#333">EconData</text>
      <text x="30" y="7" font-size="3" fill="#666">Producer price index: rubber and plastic products</text>
      <rect x="192" y="12" width="28" height="72" fill="#f6f4d2"/>
      <g stroke="#e4e4e4" stroke-width=".4"><line x1="16" y1="24" x2="224" y2="24"/><line x1="16" y1="39" x2="224" y2="39"/><line x1="16" y1="54" x2="224" y2="54"/><line x1="16" y1="69" x2="224" y2="69"/></g>
      <polyline fill="none" stroke="#3f61b0" stroke-width=".8" points="16,68 30,67 44,64 58,60 72,56 86,52 100,48 114,42 128,43 142,44 156,45 170,46 184,47 194,49 202,50 210,46 216,40 220,30 224,20"/>
      <g font-size="2.8" fill="#777"><text x="20" y="90">2008</text><text x="50" y="90">2010</text><text x="80" y="90">2012</text><text x="110" y="90">2014</text><text x="140" y="90">2016</text><text x="170" y="90">2018</text><text x="200" y="90">2021</text></g>
      <text x="6" y="96" font-size="2.6" fill="#777">Shaded areas indicate recessions</text>
      <text x="98" y="96" font-size="2.6" fill="#777">Source: labor statistics office</text>
    </svg>
  </div>

  <div class="footer-call">
    <svg viewBox="0 0 16 26"><path d="M13 2 C3 4 2 22 13 24" fill="none" stroke="#fff" stroke-width="2.6" stroke-linecap="round"/></svg>
    <span>Call us at <b>800-555-BOND (2663)</b></span>
  </div>
</section>

</body>
</html>
```